Professional & attention grabbing.

A business card design, front and back. I already have a logo I will attach, but I am open to something new as well.
Things to include:
Name:
Title:
Phone:
Email:
Wanting something that is professional but attention grabbing.
Also we do a lot of work using drones on natural gas pipelines (leading the future)if you want to include any of that. I'm open to ideas.
Target Market(s)
Natural gas transmission industry / greenhouse gas mitigation industry
Industry/Entity Type
Business
Contact Information for Business Card
All details have been conveyed above.
Colors
Designer to choose colors to be used in the design.
Look and feel
Each slider illustrates characteristics of the customer's brand and the style your logo design should communicate.

```html
<!DOCTYPE html>
<html lang="en">
<head>
<meta charset="utf-8">
<title>Vantor Field Inspections – Business Card</title>
<link rel="stylesheet" href="https://fonts.googleapis.com/css2?family=Roboto+Condensed:wght@300;400;700&display=swap">
<style>
  :root {
    --stage: #1d1d1f;
    --card-dark: #3b3b3d;
    --card-light: #ffffff;
    --brand-red: #c9252b;
    --ink-dark: #4a4a4c;
    --ink-light: #f2f2f2;
    --ink-muted: #6d6d70;
  }
  * { box-sizing: border-box; margin: 0; padding: 0; }
  html, body { width: 1200px; height: 950px; overflow: hidden; background: var(--stage); }
  body { font-family: "Roboto Condensed", "Arial Narrow", sans-serif; position: relative; }

  .card {
    position: absolute;
    left: 250px;
    width: 700px;
    height: 400px;
    border-radius: 4px;
    overflow: hidden;
    box-shadow: 0 18px 40px rgba(0,0,0,.55);
  }
  .card--front { top: 45px; background: var(--card-dark); }
  .card--back  { top: 505px; background: var(--card-light); }

  /* front */
  .front-accent { position: absolute; left: 0; bottom: 0; width: 340px; height: 260px; }
  .contact {
    position: absolute;
    top: 48px;
    right: 52px;
    text-align: right;
    color: var(--ink-light);
  }
  .contact__name { color: var(--brand-red); font-size: 26px; font-weight: 400; letter-spacing: 1px; }
  .contact__title { font-size: 20px; font-weight: 400; letter-spacing: 1px; margin-bottom: 14px; }
  .contact__line {
    display: flex; justify-content: flex-end; align-items: center; gap: 10px;
    font-size: 19px; font-weight: 300; line-height: 30px;
  }
  .contact__icon { width: 16px; height: 16px; flex: none; }

  /* back */
  .brand {
    position: absolute;
    top: 130px; left: 0; right: 0;
    display: flex; flex-direction: column; align-items: center;
  }
  .brand__row { display: flex; align-items: center; gap: 14px; }
  .brand__mark { width: 30px; height: 30px; background: var(--brand-red); }
  .brand__name { font-size: 78px; font-weight: 700; color: var(--ink-dark); line-height: 1; letter-spacing: 1px; }
  .brand__tagline { margin-top: 10px; font-size: 17px; font-weight: 400; letter-spacing: 3px; color: var(--ink-dark); }
  .web {
    position: absolute;
    bottom: 34px; left: 0; right: 0;
    text-align: center;
    font-size: 15px; font-weight: 300; letter-spacing: 8px; color: var(--ink-muted);
  }
</style>
</head>
<body>
  <section class="card card--front" aria-label="Card front">
    <svg class="front-accent" viewBox="0 0 340 260" aria-hidden="true">
      <polygon points="0,60 0,260 200,260" fill="var(--brand-red)"/>
    </svg>
    <div class="contact">
      <p class="contact__name">MARA LIND</p>
      <p class="contact__title">PRESIDENT</p>
      <p class="contact__line">555 0142 7788
        <svg class="contact__icon" viewBox="0 0 16 16"><rect width="16" height="16" rx="2" fill="var(--brand-red)"/><path d="M5 4h2l1 2.5-1.2.8a6 6 0 0 0 2 2l.8-1.2L12 9v2a1 1 0 0 1-1 1A7 7 0 0 1 4 5a1 1 0 0 1 1-1z" fill="#fff"/></svg>
      </p>
      <p class="contact__line">mara@vantorfield.com
        <svg class="contact__icon" viewBox="0 0 16 16"><rect width="16" height="16" rx="2" fill="var(--brand-red)"/><rect x="3.5" y="5" width="9" height="6" fill="none" stroke="#fff" stroke-width="1.2"/><path d="M3.5 5l4.5 3.5L12.5 5" fill="none" stroke="#fff" stroke-width="1.2"/></svg>
      </p>
      <p class="contact__line">www.vantorfield.com
        <svg class="contact__icon" viewBox="0 0 16 16"><circle cx="8" cy="8" r="8" fill="var(--brand-red)"/><circle cx="8" cy="8" r="4.5" fill="none" stroke="#fff" stroke-width="1.1"/><path d="M3.5 8h9M8 3.5c-2 2.5-2 6.5 0 9M8 3.5c2 2.5 2 6.5 0 9" fill="none" stroke="#fff" stroke-width="1"/></svg>
      </p>
    </div>
  </section>

  <section class="card card--back" aria-label="Card back">
    <div class="brand">
      <div class="brand__row">
        <span class="brand__mark" aria-hidden="true"></span>
        <span class="brand__name">VANTOR</span>
      </div>
      <p class="brand__tagline">FIELD INSPECTIONS</p>
    </div>
    <p class="web">www.vantorfield.com</p>
  </section>
</body>
</html>
```